FLyer

We need A4 tri-fold flyers which matches the colours of existing company logo.
We are a physiotherapy clinic wanting to promote
1. who we are
2. what we treat (conditions or injuries)
3. how we treat ( manual therapy, manipulation, acupuncture, exercise, Ultrasound/laser etc)

Industry/Entity Type

Clinic

```html
<!DOCTYPE html>
<html lang="en">
<head>
<meta charset="utf-8">
<title>Stridewell Physiotherapy Tri-fold Brochure</title>
<link href="https://fonts.googleapis.com/css2?family=Open+Sans:wght@400;600;700;800&display=swap" rel="stylesheet">
<style>
:root{
  --green:#6cb52d;
  --green-dark:#3d8b1e;
  --green-light:#a8d86a;
  --blue:#2b6db3;
  --sky-top:#9fd0f2;
  --sky-bottom:#e9f5fc;
  --paper:#ffffff;
  --paper-tint:#eef6fb;
  --ink:#4a4a4a;
  --ink-soft:#6d6d6d;
  --stage:#d4d4d4;
  --fold:rgba(0,0,0,.08);
}
*{box-sizing:border-box;margin:0;padding:0}
html,body{width:934px;height:1200px;overflow:hidden}
body{background:var(--stage);font-family:"Open Sans",Arial,sans-serif;color:var(--ink);position:relative}
.spread{position:absolute;left:67px;width:800px;height:566px;background:var(--paper);box-shadow:0 6px 18px rgba(0,0,0,.18);overflow:hidden}
.spread--outside{top:22px}
.spread--inside{top:612px}
.panel{position:absolute;top:0;width:267px;height:566px;overflow:hidden;background:linear-gradient(180deg,var(--paper-tint),var(--paper) 60%)}
.panel--1{left:0}
.panel--2{left:267px;border-left:1px solid var(--fold)}
.panel--3{left:534px;width:266px;border-left:1px solid var(--fold)}
.photo{position:absolute;left:0;width:100%}
.swoosh{position:absolute;left:0;width:100%;pointer-events:none}

/* Outside: conditions panel */
.badge-circle{position:absolute;border-radius:50%;background:var(--green);border:3px solid #fff;box-shadow:0 2px 6px rgba(0,0,0,.2);color:#fff;display:flex;flex-direction:column;align-items:center;justify-content:center;font-weight:800;text-transform:uppercase;line-height:1}
.badge-circle--treat{left:14px;top:118px;width:74px;height:74px;font-size:17px}
.condition-list{position:absolute;right:14px;top:168px;text-align:right}
.condition-list h3{color:var(--green-dark);font-size:12.5px;font-weight:700;margin-top:10px}
.condition-list h3:first-child{margin-top:0}
.condition-list li{list-style:none;font-size:10px;line-height:1.45;color:var(--ink)}

/* Outside: contact panel */
.contact-intro{position:absolute;left:22px;right:18px;top:208px;font-size:12px;line-height:1.4;color:var(--blue)}
.contact-intro strong{color:var(--green-dark);font-weight:600}
.brand{display:flex;align-items:center;gap:7px;color:var(--green);font-weight:800;letter-spacing:-.3px}
.brand__dot{border-radius:50%;background:var(--green);flex:none}
.brand--contact{position:absolute;left:22px;top:262px;font-size:24px}
.brand--contact .brand__dot{width:26px;height:26px}
.contact-rule{position:absolute;left:22px;right:22px;top:302px;height:1px;background:var(--green-light)}
.contact-details{position:absolute;left:22px;top:314px;font-size:10px;line-height:1.5;color:var(--ink-soft)}
.contact-details p+p{margin-top:9px}
.member{position:absolute;top:470px;display:flex;flex-direction:column;align-items:center;gap:3px;font-size:9px;font-weight:700}
.member--a{left:28px;color:#d12b2b}
.member--b{left:118px;color:var(--blue)}
.member__shape{width:40px;height:30px;border-radius:6px;background:#e2eaf3;border:2px solid currentColor}
.member--b .member__shape{border-radius:50%;width:32px;height:32px}

/* Outside: cover */
.cover-title{position:absolute;left:0;right:0;top:22px;text-align:center;font-weight:800;line-height:1.05;z-index:2}
.cover-title span{display:block}
.cover-title .t1{color:var(--green-dark);font-size:15px}
.cover-title .t2{color:#b5e06a;font-size:19px}
.cover-title .t3{color:var(--green);font-size:24px;text-shadow:0 1px 2px rgba(255,255,255,.7)}
.brand--cover{position:absolute;left:36px;top:454px;font-size:27px}
.brand--cover .brand__dot{width:30px;height:30px}
.cover-web{position:absolute;left:0;right:0;top:502px;text-align:center;color:var(--green);font-size:10.5px;font-weight:600}

/* Inside: intro */
.intro-head{position:absolute;left:20px;right:20px;top:160px;text-align:center;font-size:13px;font-weight:700;line-height:1.2;color:var(--green-dark)}
.intro-head em{font-style:normal;color:var(--green)}
.brand--intro{position:absolute;left:44px;top:212px;font-size:23px}
.brand--intro .brand__dot{width:25px;height:25px}
.intro-body{position:absolute;left:18px;right:18px;top:258px;text-align:center;font-size:9.4px;line-height:1.42;color:var(--green-dark)}
.intro-body p+p{margin-top:6px}

/* Inside: steps */
.step{position:absolute;left:0;right:10px;display:flex;gap:10px;align-items:flex-start}
.step--1{top:28px}.step--2{top:112px}.step--3{top:196px}
.step__flag{flex:none;width:82px;height:56px;background:var(--green);color:#fff;clip-path:polygon(0 0,100% 0,88% 50%,100% 100%,0 100%);display:flex;flex-direction:column;justify-content:center;padding-left:8px;text-transform:uppercase;font-weight:800;line-height:1}
.step__flag small{font-size:8px;letter-spacing:1px}
.step__flag b{font-size:19px}
.step h4{color:var(--green-dark);font-size:12px;font-weight:700;margin-top:2px}
.step p{font-size:8.8px;line-height:1.35;color:var(--ink-soft)}
.badge-circle--how{right:10px;top:302px;width:86px;height:86px;font-size:15px;background:var(--green-dark);z-index:3}

/* Inside: treatments */
.treatments{position:absolute;left:16px;right:16px;top:22px;text-align:center}
.treatments li{list-style:none;margin-bottom:9px}
.treatments h5{color:var(--green);font-size:11px;font-weight:800;line-height:1.2}
.treatments p{font-size:8.6px;line-height:1.3;color:var(--ink-soft)}
</style>
</head>
<body>

<section class="spread spread--outside" aria-label="Brochure outside">
  <div class="panel panel--1">
    <div class="photo" style="top:0;height:120px;background:linear-gradient(180deg,#c9a58a,#e8d7c9 70%,#f3f3f3)" role="img" aria-label="Photo of a runner's legs in motion"></div>
    <svg class="swoosh" style="top:92px" width="267" height="70" viewBox="0 0 267 70"><path d="M0 40 C80 0 180 -5 267 20 L267 70 L0 70Z" fill="#eef6fb"/><path d="M0 40 C80 0 180 -5 267 20" fill="none" stroke="var(--green)" stroke-width="5"/></svg>
    <div class="badge-circle badge-circle--treat"><span>We</span><span>Treat</span></div>
    <div class="condition-list">
      <h3>Spinal conditions</h3>
      <ul><li>Back /neck pain, Headaches</li><li>Disc bulge/protrusion</li><li>Unstable pelvis or spine</li><li>Nerve impingement</li></ul>
      <h3>Sports injuries</h3>
      <ul><li>ACL rehab</li><li>Post-op rehab</li><li>Muscle strain/tear</li><li>Rotator cuff</li><li>Sports related back pain</li></ul>
      <h3>RSI (repetitive strain injuries)</h3>
      <ul><li>Tennis elbow</li><li>Muscle strain</li><li>Achilles tendonosis</li><li>Rotator cuff tendonosis</li></ul>
    </div>
    <div class="photo" style="top:420px;height:146px;background:linear-gradient(160deg,#e6c3a8,#c99a7a 55%,#3a3a3a)" role="img" aria-label="Photo of a physiotherapist treating a patient's knee"></div>
    <svg class="swoosh" style="top:400px" width="267" height="50" viewBox="0 0 267 50"><path d="M0 0 L267 0 L267 14 C170 44 80 44 0 30Z" fill="#fff"/><path d="M267 14 C170 44 80 44 0 30" fill="none" stroke="var(--green)" stroke-width="4"/></svg>
  </div>

  <div class="panel panel--2">
    <div class="photo" style="top:0;height:200px;background:linear-gradient(180deg,#d8e3e6,#b7c8cf 60%,#8aa4ae)" role="img" aria-label="Photo of a physiotherapist guiding a patient through a leg exercise"></div>
    <svg class="swoosh" style="top:150px" width="267" height="60" viewBox="0 0 267 60"><path d="M0 30 C90 60 180 0 267 15 L267 60 L0 60Z" fill="#eef6fb"/><path d="M0 30 C90 60 180 0 267 15" fill="none" stroke="var(--green)" stroke-width="5"/></svg>
    <p class="contact-intro">To arrange an <strong>appointment</strong> or to speak to a <strong>physiotherapist</strong>, please <strong>contact us.</strong></p>
    <div class="brand brand--contact"><span class="brand__dot"></span>Stridewell</div>
    <div class="contact-rule"></div>
    <div class="contact-details">
      <p>Unit 4, Harbour Walk<br>212 Elm Parade, Northbay 2090</p>
      <p>Phone: (02) 5550 1842<br>Fax: &nbsp;&nbsp;&nbsp;(02) 5550 1843<br>hello@stridewellphysio.example<br>www.stridewellphysio.example</p>
    </div>
    <svg class="swoosh" style="top:405px" width="267" height="50" viewBox="0 0 267 50"><path d="M0 10 C90 45 180 40 267 20" fill="none" stroke="var(--green)" stroke-width="4"/></svg>
    <div class="member member--a"><span class="member__shape"></span>Member</div>
    <div class="member member--b"><span class="member__shape"></span>Member</div>
  </div>

  <div class="panel panel--3">
    <div class="photo" style="top:0;height:420px;background:radial-gradient(circle at 55% 22%,#fffbe6 0,#d7ecfa 22%,var(--sky-top) 55%,#7fb3d9 100%)" role="img" aria-label="Photo of a woman running outdoors under a bright sunny sky"></div>
    <h1 class="cover-title"><span class="t1">Get Well</span><span class="t2">Move Well</span><span class="t3">Freedom Again</span></h1>
    <svg class="swoosh" style="top:380px" width="266" height="70" viewBox="0 0 266 70"><path d="M0 40 C90 10 180 5 266 25 L266 70 L0 70Z" fill="#fff"/><path d="M0 40 C90 10 180 5 266 25" fill="none" stroke="var(--green)" stroke-width="8"/></svg>
    <div class="brand brand--cover"><span class="brand__dot"></span>Stridewell</div>
    <p class="cover-web">www.stridewellphysio.example</p>
    <svg class="swoosh" style="top:530px" width="266" height="36" viewBox="0 0 266 36"><path d="M0 36 C90 10 180 4 266 14 L266 36Z" fill="var(--green)"/></svg>
  </div>
</section>

<section class="spread spread--inside" aria-label="Brochure inside">
  <div class="panel panel--1">
    <div class="photo" style="top:0;height:140px;background:linear-gradient(150deg,#e8cdb8,#d4a98d 50%,#f1f1f1)" role="img" aria-label="Photo of a therapist stretching a patient's arm"></div>
    <svg class="swoosh" style="top:100px" width="267" height="60" viewBox="0 0 267 60"><path d="M0 45 C90 5 180 0 267 30 L267 60 L0 60Z" fill="#eef6fb"/><path d="M0 45 C90 5 180 0 267 30" fill="none" stroke="var(--green)" stroke-width="5"/></svg>
    <h2 class="intro-head">You do not need a <em>doctor's referral</em> to see a physiotherapist at</h2>
    <div class="brand brand--intro"><span class="brand__dot"></span>Stridewell</div>
    <div class="intro-body">
      <p>In the clinic we have the latest clinically-proven equipments which will improve the accuracy in the diagnosis of your conditions and pain. You will be assessed by the experienced physiotherapists using a range of musculoskeletal and orthopaedic tests.</p>
      <p>As there isn't a magic tablet for all conditions, neither is there a treatment technique for everybody. At Stridewell our physiotherapists adopt a range of treatment techniques via continuing professional development and education to ensure we get the patients the best treatment outcomes.</p>
      <p>We recognise that people have different goals and expectations in life so do they have for their treatments.</p>
    </div>
  </div>

  <div class="panel panel--2">
    <div class="step step--1"><div class="step__flag"><small>Step</small><b>One</b></div><div><h4>Assessment</h4><p>Effective treatments come with accurate diagnosis</p></div></div>
    <div class="step step--2"><div class="step__flag"><small>Step</small><b>Two</b></div><div><h4>Treatment</h4><p>Effective treatments also require choosing the right treatment techniques</p></div></div>
    <div class="step step--3"><div class="step__flag"><small>Step</small><b>Three</b></div><div><h4>Education</h4><p>You will get more than just treatments. You are educated in every possible way to reduce the timeframe of the recovery</p></div></div>
    <svg class="swoosh" style="top:280px" width="267" height="60" viewBox="0 0 267 60"><path d="M0 10 C90 40 180 40 267 20" fill="none" stroke="var(--green)" stroke-width="4"/></svg>
    <div class="photo" style="top:300px;height:266px;background:linear-gradient(170deg,#f4efe9,#cfe1ee 40%,#6fa6d6 75%,#e9c7ad)" role="img" aria-label="Photo of a physiotherapist helping an older patient raise her arm"></div>
    <div class="badge-circle badge-circle--how"><span>How</span><span>do we</span><span>treat</span></div>
  </div>

  <div class="panel panel--3">
    <ul class="treatments">
      <li><h5>Acupuncture/Dry-needling</h5><p>Eases pain and swelling, speeds healing of muscle strain and tension</p></li>
      <li><h5>Manual therapy &amp; spinal manipulation</h5><p>Mulligan and Maitland techniques, muscle energy release</p></li>
      <li><h5>Taping/strapping: Sports taping, Kinesiology taping</h5><p>Supports joints for sport and work, speeds return to play</p></li>
      <li><h5>Customised Orthotics</h5><p>Correct foot and knee pain through walking and running analysis and custom orthotic fitting</p></li>
      <li><h5>Electrical Therapy; ultrasound, laser, traction, electrical stimulation</h5><p>Reduces pain and swelling, improves healing after muscle tension</p></li>
      <li><h5>Casting and splinting</h5><p>Post fracture and high grade ligament sprain support</p></li>
      <li><h5>Pelvic floor/incontinence training</h5><p>Using real-time ultrasound device</p></li>
      <li><h5>One on one pilates exercise</h5><p>Pelvic floor and core stability training with real time ultrasound</p></li>
    </ul>
  </div>
</section>

</body>
</html>
```